Blue Heron Courier & Delivery Services needs a flyer

We need an introductory flyer for a new company based in Yellowknife, Northwest Territories,Canada. Our company name is Blue Heron Courier & Delivery Services. We will be handling envelopes and small packages up to 20 pounds. We expect 20 percent of our business to come from residential customers and 80 percent from the business community including lawyers, doctors, engineers and government offices. The main message that we will try to convey in this flyer is that we are a new and exciting company that promises to make 100% customer satisfaction our number one goal. I would like the layout to be elegant and simple and certainly not cluttered. It will be a single sided flyer. Text should be easy to read and most likely at most two fonts. I would like one stunning image or photo relating to the courier business and message. There should be plenty of white space throughout the flyer and nice margins on all sides. I would like my flyer to be 8.5 inches by 11 inches and it should read from top to bottom. . I would like a nice big bold headline that in some way mentions " Special Offer- Up to 100% Off. You can change the wording if you have a better idea. Throughout the flyer you can highlight and italicize for emphasis. Please try to use bullet points for my five main reasons for hiring our company which are: you will be 100% satisfied with each delivery or you will be given a complete refund no questions asked, your envelope or package will be delivered on time every time, you will always be treated throughout the delivery process in a professional manner, you will be given the widest selection in Yellowknife of price points and delivery options , you can trust us with your most important and time sensitive deliveries. Try to incorporate something next to these five points to really draw attention like a check mark, star etc.... I would prefer if my company name and contact info is in the bottom third of the flyer. My email is blueheroncourieryk@mailbox-example.net. My phone number is 867-312-7794. It might be a good idea to have my phone number also at the top of the flyer someplace after the headline saying like Call Now!!! you can use boxes, borders and contrasting bold colors to bring flyer to life. I have a testimonial from a business owner that I dealt with when I ran another business which would be nice to have included . " While receiving daily deliveries for 18 years from Calvin Marsh I found him to be punctual , reliable and efficient " Glen Potter, owner of Potter and Lindqvist Trading LTD, Yellowknife,NWT. I thought perhaps at the top of flyer after the headline perhaps in some way you could say Yellowknife's newest and best courier and delivery service is pleased to offer the following stunning discounts: then you could list the three special offers: 1) First 5 businesses to book regular scheduled deliveries will get 100% off their first delivery. 2) First 5 businesses to book a single delivery will get 50% off that delivery. 3) First 5 residential customers to book a delivery will receive 25% off that delivery. I thought you could mention my name somewhere. Calvin Marsh. Owner has lived in Yellowknife for 42 years and has 20 years experience doing performing important and time sensitive deliveries. Perhaps you could mention somewhere that we will have a couple of ongoing discounts also which will be 1) seniors discounts. 2) regular scheduled deliveries discounts. I have suggested colors but if you have other ideas I would certainly look at them. Our business tag line is. On Time Every Time
Target Market(s)
Business owners typically males 30-50 years old
Industry/Entity Type
Delivery Service
Requirements
Must have
- Done in CMYK mode sufficient bleed size for printing
Nice to have
- Nothing set in stone. I recently had my logo design uploaded to this brief. It is up to you if you feel it should be included in the flyer.
Should not have
- I am willing to look at any design

```html
<!DOCTYPE html>
<html lang="en">
<head>
<meta charset="utf-8">
<title>Blue Heron Courier &amp; Delivery Services – Flyer</title>
<link rel="stylesheet" href="https://fonts.googleapis.com/css2?family=Open+Sans:wght@400;600;700&display=swap">
<style>
  :root {
    --backdrop: #d6d6d6;
    --navy: #1f3c8c;
    --yellow: #f6ec34;
    --yellow-soft: #f9f27a;
    --pink: #e8455a;
    --charcoal: #3b3b3b;
    --white: #ffffff;
    --sky-top: #2b3550;
    --sky-mid: #6f86a8;
    --sky-low: #c9d6e4;
  }
  * { margin: 0; padding: 0; box-sizing: border-box; }
  html, body {
    width: 1200px; height: 795px; overflow: hidden;
    background: var(--backdrop);
    font-family: "Open Sans", sans-serif;
  }
  .flyer {
    position: absolute; left: 340px; top: 27px;
    width: 520px; height: 740px;
    background: var(--white);
    overflow: hidden;
    box-shadow: 0 2px 8px rgba(0,0,0,0.15);
  }
  .flyer-shapes { position: absolute; inset: 0; }
  .brand-box {
    position: absolute; left: 338px; top: 12px; width: 156px; height: 210px;
    background: var(--yellow);
    text-align: center;
  }
  .brand-box::before, .brand-box::after {
    content: ""; position: absolute; left: 50%; transform: translateX(-50%);
    width: 60px; height: 6px; background: var(--navy);
  }
  .brand-box::before { top: 0; }
  .brand-box::after { bottom: 0; }
  .brand-name {
    margin-top: 24px; padding: 0 10px;
    font-size: 12px; font-weight: 700; line-height: 1.2;
    color: var(--pink); text-transform: uppercase;
  }
  .offer-label {
    margin-top: 28px;
    font-size: 17px; font-weight: 700; color: var(--navy);
  }
  .offer-value {
    font-size: 24px; font-weight: 600; line-height: 1.1; color: var(--pink);
  }
  .content { position: absolute; left: 24px; top: 428px; width: 326px; }
  .headline { font-size: 22px; font-weight: 600; color: var(--pink); }
  .intro {
    margin-top: 6px; font-size: 8.5px; line-height: 10.5px; color: var(--charcoal);
  }
  .reasons { margin-top: 16px; list-style: none; }
  .reasons li {
    font-size: 9px; line-height: 14px; font-weight: 600; color: var(--pink);
    white-space: nowrap;
  }
  .phone-row {
    position: absolute; left: 24px; top: 630px; width: 336px;
    display: flex; align-items: center; gap: 8px;
  }
  .phone { font-size: 15px; font-weight: 700; color: var(--pink); white-space: nowrap; }
  .phone-bar { flex: 1; height: 14px; background: var(--pink); }
  .email {
    position: absolute; left: 24px; top: 654px;
    font-size: 11px; font-weight: 600; color: var(--navy);
  }
  .owner-note {
    position: absolute; left: 0; top: 681px; width: 520px; height: 22px;
    padding-left: 20px; line-height: 22px; white-space: nowrap;
    font-size: 9px; color: var(--white);
  }
  .owner-photo {
    position: absolute; left: 364px; top: 475px; width: 114px; height: 206px;
    background: #111111;
    border-radius: 40px 40px 0 0;
    display: flex; align-items: center; justify-content: center;
    text-align: center;
  }
  .owner-photo span {
    font-size: 13px; font-weight: 700; line-height: 1.35; color: var(--white);
  }
</style>
</head>
<body>
  <main class="flyer">
    <svg class="flyer-shapes" viewBox="0 0 520 740" width="520" height="740">
      <defs>
        <linearGradient id="skyGradient" x1="0" y1="0" x2="0" y2="1">
          <stop offset="0" stop-color="#2b3550"/>
          <stop offset="0.45" stop-color="#6f86a8"/>
          <stop offset="0.8" stop-color="#c9d6e4"/>
          <stop offset="1" stop-color="#4a5560"/>
        </linearGradient>
      </defs>
      <polygon class="hero-photo" role="img" aria-label="Photo of a delivery truck speeding along a highway under a moonlit sky" points="0,0 520,0 520,305 0,400" fill="url(#skyGradient)"/>
      <polygon class="top-corner" points="60,0 520,0 520,38 340,60" fill="#ffffff"/>
      <polygon class="top-stripe" points="30,0 60,0 340,60 520,38 520,46 336,66" fill="#1f3c8c"/>
      <line class="band-gap" x1="0" y1="399" x2="520" y2="302" stroke="#ffffff" stroke-width="4"/>
      <polygon class="accent-band" points="0,402 520,305 520,410 0,420" fill="#1f3c8c"/>
      <polygon class="content-panel" points="0,420 520,410 520,681 0,681" fill="#f9f27a"/>
      <rect class="owner-strip" x="0" y="681" width="520" height="22" fill="#3b3b3b"/>
      <rect class="footer-band" x="0" y="703" width="520" height="37" fill="#1f3c8c"/>
    </svg>

    <section class="brand-box">
      <p class="brand-name">Blue Heron Courier &amp; Delivery Services</p>
      <p class="offer-label">SPECIAL OFFER</p>
      <p class="offer-value">Up to 100%<br>Off</p>
    </section>

    <section class="content">
      <h1 class="headline">We fight for your rights!</h1>
      <p class="intro">Yellowknife's newest and best courier and delivery service is pleased to offer these stunning discounts: the first 5 businesses to book regular scheduled deliveries get 100% off their first delivery, the first 5 businesses to book a single delivery get 50% off, and the first 5 residential customers get 25% off.</p>
      <ul class="reasons">
        <li>100% satisfaction or a full refund, no questions asked.</li>
        <li>Your envelope or package delivered on time every time.</li>
        <li>Professional treatment through every step of delivery.</li>
        <li>Yellowknife's widest choice of prices and delivery options.</li>
        <li>Trusted with your most important, time sensitive deliveries.</li>
      </ul>
    </section>

    <div class="phone-row">
      <span class="phone">867-312-7794</span>
      <span class="phone-bar"></span>
    </div>
    <p class="email">blueheroncourieryk@mailbox-example.net</p>

    <div class="owner-photo" role="img" aria-label="Placeholder for a portrait of the owner">
      <span>Owner<br>Photo<br>Here!</span>
    </div>

    <p class="owner-note">Meet Calvin Marsh. The Owner has lived in Yellowknife for 42 years and has 20 years experience.</p>
  </main>
</body>
</html>
```